Stationery & Business Card Design For A Mobile Ultrasound Company
Ridgecrest Sonar Partners, Inc.
Professional
Martin L. Povich
Clinical Director
3187 Hawthorn Lane NE
Larkmere, NV 44892
ridgecrestsonarpartners@mailnest.example
www.ridgecrestsonarpartners.example

```html
<!DOCTYPE html>
<html lang="en">
<head>
<meta charset="utf-8">
<title>Ridgecrest Sonar Partners – Business Card</title>
<link rel="stylesheet" href="https://fonts.googleapis.com/css2?family=Montserrat:wght@500&family=Open+Sans:wght@400&display=swap">
<style>
  :root {
    --page-bg: #eceae6;
    --card-bg: #ffffff;
    --brand-blue: #2b78b6;
    --band-blue: #2572b2;
    --band-blue-light: #3a8dca;
    --panel-blue: #1f66a3;
    --accent-red: #d2323b;
    --ink: #3a4a5a;
    --band-text: #ffffff;
  }
  * { margin: 0; padding: 0; box-sizing: border-box; }
  html, body {
    width: 1200px; height: 818px; overflow: hidden;
    background: var(--page-bg);
  }
  .card {
    position: absolute; left: 84px; top: 139px;
    width: 1032px; height: 624px;
    background: var(--card-bg);
    box-shadow: 0 6px 18px rgba(0,0,0,0.18);
    overflow: hidden;
  }
  .brand {
    position: absolute; left: 0; right: 0; top: 104px;
    display: flex; align-items: center; justify-content: center; gap: 20px;
  }
  .brand-square { width: 40px; height: 40px; background: var(--accent-red); flex: none; }
  .brand-name {
    font-family: "Montserrat", sans-serif; font-weight: 500;
    font-size: 50px; line-height: 66px; letter-spacing: 1px; color: var(--brand-blue);
    white-space: nowrap;
  }
  .holder {
    position: absolute; left: 271px; top: 326px;
    font-family: "Open Sans", sans-serif; color: var(--ink);
    white-space: nowrap; display: flex; align-items: baseline; gap: 10px;
  }
  .holder-name { font-size: 30px; color: var(--brand-blue); letter-spacing: 0.5px; }
  .holder-title { font-size: 22px; }
  .rule-red {
    position: absolute; left: 0; right: 0; top: 389px; height: 5px;
    background: var(--accent-red);
  }
  .band {
    position: absolute; left: 0; right: 0; top: 401px; bottom: 0;
    background: linear-gradient(180deg, var(--band-blue-light), var(--band-blue));
  }
  .band-panel {
    position: absolute; left: 0; top: 0; bottom: 0; width: 190px;
    background: var(--panel-blue);
  }
  .band-mark {
    position: absolute; left: 62px; top: 66px; width: 66px; height: 66px;
    background: rgba(210,50,59,0.6);
  }
  .band-divider {
    position: absolute; left: 192px; top: 0; bottom: 0; width: 5px;
    background: #ffffff;
  }
  .contact {
    position: absolute; left: 262px; top: 18px;
    font-family: "Open Sans", sans-serif; color: var(--band-text);
    font-size: 21px; line-height: 36px; white-space: nowrap;
  }
  .address { font-size: 24px; margin-bottom: 6px; }
  .contact-row { display: flex; }
  .contact-item { display: flex; align-items: center; gap: 10px; }
  .contact-item.phone { width: 262px; }
  .contact-item svg { width: 18px; height: 18px; flex: none; fill: none; stroke: var(--band-text); stroke-width: 2; }
</style>
</head>
<body>
  <div class="card">
    <div class="brand">
      <span class="brand-square"></span>
      <span class="brand-name">Ridgecrest Sonar Partners</span>
    </div>

    <div class="holder">
      <span class="holder-name">MARTIN L. POVICH</span><span class="holder-title">Clinical Director</span>
    </div>

    <div class="rule-red"></div>

    <div class="band">
      <div class="band-panel"><span class="band-mark"></span></div>
      <div class="band-divider"></div>
      <div class="contact">
        <div class="address">3187 Hawthorn Lane NE, Larkmere, NV 44892</div>
        <div class="contact-row">
          <div class="contact-item phone">
            <svg viewBox="0 0 20 20"><path d="M5 2 L8 2 L9 6 L7 8 Q9 12 12 13 L14 11 L18 12 L18 15 Q17 18 14 18 Q3 16 2 5 Q2 2 5 2 Z"/></svg>
            <span>555-555-0174</span>
          </div>
          <div class="contact-item">
            <svg viewBox="0 0 20 20"><rect x="2" y="4" width="16" height="12" rx="1"/><path d="M2 5 L10 11 L18 5"/></svg>
            <span>ridgecrestsonarpartners@mailnest.example</span>
          </div>
        </div>
        <div class="contact-row">
          <div class="contact-item phone">
            <svg viewBox="0 0 20 20"><rect x="5" y="1" width="10" height="18" rx="2"/><path d="M8 16 L12 16"/></svg>
            <span>555-555-0196</span>
          </div>
          <div class="contact-item">
            <svg viewBox="0 0 20 20"><circle cx="10" cy="10" r="8"/><ellipse cx="10" cy="10" rx="3.5" ry="8"/><path d="M2 10 L18 10"/></svg>
            <span>www.ridgecrestsonarpartners.example</span>
          </div>
        </div>
      </div>
    </div>
  </div>
</body>
</html>
```